Classic and neutral book cover design

We are looking for a classic and neutral book cover design to be used as the template for a series of books to be published. We are hence looking for a template that will allow us to easily change the title name for all books in this series.
The use of very few colours (black and white is welcome) and few design elements is a big bonus. As a source of inspiration we would like to ask you to view the very simple and
If you think you have a cool idea that can add a twist to the formal classic look don't hesitate. Go for it !
Work will be done for a 30 year old Sweden based cultural non-profit called VĂ©lra (www.velrafoundation.example). We work with the publishing and supporting of post-modern art and literature addressing contemporary topics but are also involved in assisting projects of cultural preservation.
Target Market(s)
The audience is expected to have some form of interest in culture but could range from hobbyist readers to tenure track scholars
Industry/Entity Type
Non-Profit
Requirements
Must have
- General:
- Classic and neutral feel
- Preferably very simple and few shapes
- usage of few colours (black and white is welcome)
Information to be displayed on the cover is:
- Author
- Title
- type of work e.g. play/novel (optional)
- publishing house (in this case "Velra Publishing")
Nice to have
- ideas to prevent it from become boring are of course welcome
Should not have
- - too many colours

```html
<!DOCTYPE html>
<html lang="en">
<head>
<meta charset="utf-8">
<title>Grey Harbour — Book Cover</title>
<link rel="stylesheet" href="https://fonts.googleapis.com/css2?family=Cinzel:wght@400;500&family=Italianno&display=swap">
<style>
  :root {
    --backdrop: #b9b9b9;
    --paper: #ffffff;
    --ink: #000000;
    --reverse: #ffffff;
    --shadow: rgba(0, 0, 0, 0.45);
  }
  html, body {
    margin: 0;
    padding: 0;
    width: 1200px;
    height: 812px;
    overflow: hidden;
    background: var(--backdrop);
  }
  .stage {
    position: relative;
    width: 1200px;
    height: 812px;
  }
  .cover {
    position: absolute;
    left: 342px;
    top: 82px;
    width: 516px;
    height: 648px;
    background: var(--paper);
    box-shadow: 4px 4px 8px var(--shadow);
  }
  .cover__author {
    position: absolute;
    top: 148px;
    left: 0;
    width: 100%;
    margin: 0;
    text-align: center;
    font-family: "Italianno", cursive;
    font-weight: 400;
    font-size: 36px;
    line-height: 40px;
    color: var(--ink);
  }
  .cover__title-band {
    position: absolute;
    top: 195px;
    left: 0;
    width: 100%;
    height: 47px;
    background: var(--ink);
    display: flex;
    align-items: center;
    justify-content: center;
  }
  .cover__title {
    margin: 0;
    font-family: "Cinzel", serif;
    font-weight: 400;
    font-size: 40px;
    line-height: 47px;
    letter-spacing: 1px;
    color: var(--reverse);
  }
  .cover__genre {
    position: absolute;
    top: 268px;
    left: 0;
    width: 100%;
    height: 20px;
    display: flex;
    align-items: center;
  }
  .cover__rule {
    flex: 1;
    height: 10px;
    box-sizing: border-box;
    border-top: 2.5px solid var(--ink);
    border-bottom: 2px solid var(--ink);
  }
  .cover__genre-label {
    padding: 0 12px;
    font-family: "Cinzel", serif;
    font-weight: 500;
    font-size: 13px;
    letter-spacing: 0.5px;
    color: var(--ink);
  }
  .cover__publisher {
    position: absolute;
    top: 526px;
    left: 0;
    width: 100%;
    margin: 0;
    text-align: center;
    font-family: "Cinzel", serif;
    font-weight: 500;
    font-size: 10px;
    letter-spacing: 0.4px;
    color: var(--ink);
  }
</style>
</head>
<body>
  <main class="stage">
    <article class="cover">
      <p class="cover__author">Edvin Sjöhamn</p>
      <div class="cover__title-band">
        <h1 class="cover__title">Grey Harbour</h1>
      </div>
      <div class="cover__genre">
        <span class="cover__rule"></span>
        <span class="cover__genre-label">PLAY</span>
        <span class="cover__rule"></span>
      </div>
      <p class="cover__publisher">VELRA PUBLISHING</p>
    </article>
  </main>
</body>
</html>
```